Business cards for property management company

Need new business cards designed for our property management company and rental community, Blue Fern Commons. These cards will be primarily picked up by rental applicants.

May be single or double sided design.

I need cards for two different people, listed below. The design can be the same for both, and the only information that will be different is name and email address.

Industry/Entity Type

Property Management

Requirements
Must have
• US standard business card - 2''x3.5'' horizontal design.

1. Logo (attached). The text does not have to stay below the logo, but the card does need to say "Blue Fern Commons" somewhere on it (does not have to be same font as logo, but those fonts are Americana Extra Bold and BlackJack if needed).
2. Name: one with "Paula Whitcombe" and one with "Darrell Whitcombe"
3. Email address: one with "paula@bluefernhome.com" and one with "darrell@bluefernhome.com"
4. Web address: bluefernhome.com
5. Phone: 281.604.2218
6. Address: 1783 Wexford Lane, Porterfield, Texas 77812 (zip code may me omitted, at your discretion)
Should not have
• No rounded corners or special cuts.

No bevel, emboss or shadow effects.

As a note, please do not use our website as a basis for color or design schemes. We are working on a redesign, based around the new logo (attached to brief).

```html
<!DOCTYPE html>
<html lang="en">
<head>
<meta charset="utf-8">
<title>Blue Fern Commons — Business Cards</title>
<link href="https://fonts.googleapis.com/css2?family=Libre+Baskerville:wght@400;700&display=swap" rel="stylesheet">
<style>
  :root {
    --card-teal: #00e2c3;
    --frame-teal: #1fd9c0;
    --ink-white: #ffffff;
    --sheet: #ffffff;
    --shadow: rgba(60, 60, 60, 0.55);
    --faint: rgba(255, 255, 255, 0.13);
  }
  * { box-sizing: border-box; margin: 0; padding: 0; }
  html, body { width: 1200px; height: 900px; overflow: hidden; background: var(--sheet); }
  .sheet {
    position: relative;
    width: 1200px; height: 900px;
    border: 4px solid var(--frame-teal);
    background: var(--sheet);
    font-family: "Libre Baskerville", Georgia, serif;
    color: var(--ink-white);
  }
  .card {
    position: absolute;
    background: var(--card-teal);
    overflow: hidden;
    box-shadow: 10px 10px 12px var(--shadow);
  }
  .card--logo { left: 90px; width: 370px; height: 206px; }
  .card--logo-left { top: 66px; }
  .card--logo-right { top: 340px; }
  .card--logo-center { top: 614px; }
  .card--contact { left: 540px; width: 568px; }
  .card--paula { top: 66px; height: 354px; }
  .card--darrell { top: 472px; height: 330px; }

  .brand-name {
    position: absolute;
    font-weight: 700;
    color: var(--ink-white);
    line-height: 1.15;
  }
  .brand-dot {
    position: absolute;
    border-radius: 50%;
    background: var(--ink-white);
  }
  .card--logo-left .brand-name { left: 30px; top: 58px; font-size: 27px; }
  .card--logo-left .brand-dot { left: 250px; top: 38px; width: 100px; height: 100px; }
  .card--logo-right .brand-name { right: 20px; top: 108px; font-size: 27px; text-align: right; }
  .card--logo-right .brand-dot { left: 20px; top: 22px; width: 100px; height: 100px; }
  .card--logo-center .brand-name { left: 0; right: 0; top: 132px; font-size: 22px; text-align: center; }
  .card--logo-center .brand-dot { left: 147px; top: 22px; width: 80px; height: 80px; }

  .backdrop-mark {
    position: absolute;
    border-radius: 50%;
    background: var(--faint);
  }
  .card--paula .backdrop-mark { width: 300px; height: 300px; left: 330px; top: 40px; }
  .card--darrell .backdrop-mark { width: 300px; height: 300px; left: -90px; top: 40px; }

  .line {
    position: absolute;
    left: 0; right: 0;
    text-align: center;
    white-space: nowrap;
    line-height: 1;
  }
  .person-name { font-size: 29px; letter-spacing: 3px; text-transform: uppercase; }
  .email { font-size: 17px; letter-spacing: 1px; }
  .detail { font-size: 17px; }
  .web { font-size: 23px; letter-spacing: 5px; }

  .card--paula .person-name { top: 60px; }
  .card--paula .email { top: 102px; }
  .card--paula .phone { top: 168px; }
  .card--paula .addr-1 { top: 210px; }
  .card--paula .addr-2 { top: 234px; }
  .card--paula .addr-3 { top: 258px; }
  .card--paula .web { top: 314px; }

  .card--darrell .person-name { top: 36px; }
  .card--darrell .email { top: 76px; }
  .card--darrell .phone { top: 142px; }
  .card--darrell .addr-1 { top: 180px; }
  .card--darrell .addr-2 { top: 204px; }
  .card--darrell .addr-3 { top: 228px; }
  .card--darrell .web { top: 288px; }
</style>
</head>
<body>
<main class="sheet">
  <section class="card card--logo card--logo-left" aria-label="Card front, name left">
    <p class="brand-name">Blue Fern<br>Commons</p>
    <span class="brand-dot"></span>
  </section>

  <section class="card card--logo card--logo-right" aria-label="Card front, name right">
    <p class="brand-name">Blue Fern<br>Commons</p>
    <span class="brand-dot"></span>
  </section>

  <section class="card card--logo card--logo-center" aria-label="Card front, centered">
    <span class="brand-dot"></span>
    <p class="brand-name">Blue Fern Commons</p>
  </section>

  <section class="card card--contact card--paula" aria-label="Card back, Paula Whitcombe">
    <span class="backdrop-mark"></span>
    <h2 class="line person-name">Paula Whitcombe</h2>
    <p class="line email">paula@bluefernhome.com</p>
    <p class="line detail phone">281.604.2218</p>
    <p class="line detail addr-1">1783 Wexford Lane</p>
    <p class="line detail addr-2">Porterfield, Texas</p>
    <p class="line detail addr-3">77812</p>
    <p class="line web">www.bluefernhome.com</p>
  </section>

  <section class="card card--contact card--darrell" aria-label="Card back, Darrell Whitcombe">
    <span class="backdrop-mark"></span>
    <h2 class="line person-name">Darrell Whitcombe</h2>
    <p class="line email">darrell@bluefernhome.com</p>
    <p class="line detail phone">281.604.2218</p>
    <p class="line detail addr-1">1783 Wexford Lane</p>
    <p class="line detail addr-2">Porterfield, Texas</p>
    <p class="line detail addr-3">77812</p>
    <p class="line web">www.bluefernhome.com</p>
  </section>
</main>
</body>
</html>
```